Automotive Locksmiith company needs a website design and mobile website

We need a website design and a mobile design for an automotive locksmith company called Halvern Keyworks LLC.We are based in the center of the Dallas-Fort Worth Metroplex. We have a website that was directed more towards the towing services we also offer. We would like to have it more towards our locksmith products. Our main services include:
Auto keys duplication
Cutting of new car keys
Car Lockouts
Laser key replacement
Cutting keys by code
Broken key extractions
Production of transponder keys
Key fob programming
Door lock repairs
Ignition repairs/replacement
We work on 95% of the automotive market that includes Vorla, Tessin, QRT, Pembrook, Marquenne, Dunmoral, Brask, VX, Sorvalo, Kelto, Zephrane, Oru, Hadley, Norax, Tabori, Valdrenne, Quillon, Pipo, Runel Okarawe , Brevik, Solumé, Drennhofer, Kestra.
We are one of the most affordable services in the DFW area . Our prices for transponder copies start at $35 per key. We provide services for high-end vehicles also as QRT and Valdrenne. We can program the new proximity keys for Tabori Vehicles 2013-up. We also work on the new Pell Vehicles 20-13 and up including the Pell Arden head remote key.
We would like to have a similar style to the website we already have with the option to schedule an appointment on the mobile website. This mobile application will deliver an email when a new customer is requiring the service. It will ask for Year, Make, Model , Service to be performed( Key copy, Lockout, Lost Key, Change Ignition lock, change door lock, Other services.) Description of the service to be performed, Address, Select time of service.
Our current website is halvernkeyworks.example

Reason: Need pictures of webpages inside design (about us , location etc) and mobile pictures( how website looks in Quorra / android)

Automotive

• check word attachment

```html
<!DOCTYPE html>
<html lang="en">
<head>
<meta charset="utf-8">
<title>Halvern Keyworks LLC</title>
<link rel="stylesheet" href="https://fonts.googleapis.com/css2?family=Source+Sans+3:wght@400;600;700&display=swap">
<style>
:root{
  --navy:#0f4c78;
  --navy-dark:#0d3b62;
  --navy-deep:#0a3457;
  --cyan:#1ab3e6;
  --cyan-nav:#19a5d2;
  --title:#0f4a74;
  --ink:#1b1b1b;
  --muted:#9aa3ab;
  --white:#ffffff;
  --hero-light:#c9eef8;
  --hero-mid:#8fdcf1;
}
*{box-sizing:border-box;margin:0;padding:0}
html,body{width:1200px;height:2299px;overflow:hidden}
body{position:relative;font-family:"Source Sans 3",sans-serif;color:var(--ink);background:var(--white)}
.abs{position:absolute}

/* top bar */
.topbar{left:0;top:0;width:1200px;height:44px;background:var(--navy-dark);color:var(--white);font-size:17px;font-weight:600}
.topbar .item{position:absolute;top:11px;display:flex;align-items:center;gap:10px}
.search{position:absolute;left:866px;top:8px;width:224px;height:26px;display:flex}
.search .field{flex:1;background:#d9e2ea;color:#8a98a4;font-size:13px;font-weight:400;padding:4px 8px}
.search .btn{width:36px;background:#3f6f94;display:flex;align-items:center;justify-content:center}

/* header */
.header{left:0;top:44px;width:1200px;height:117px;background:var(--white);box-shadow:0 3px 6px rgba(0,0,0,.18);z-index:2}
.brand{position:absolute;left:113px;top:62px;display:flex;align-items:center;gap:10px;font-size:24px;font-weight:600;color:var(--title);line-height:1}
.brand .mark{width:20px;height:20px;background:var(--title)}
.nav{position:absolute;left:382px;top:0;height:117px;display:flex}
.nav a{display:flex;align-items:center;height:117px;padding:0 18px;font-size:21px;color:var(--ink);text-decoration:none}
.nav a.active{background:var(--cyan-nav);color:var(--white);font-weight:600;width:93px;justify-content:center}

/* hero */
.hero{left:0;top:161px;width:1200px;height:506px;background:linear-gradient(90deg,#e6e6e6 0%,var(--hero-light) 45%,var(--hero-mid) 100%)}
.hero-photo{position:absolute;left:0;top:0;width:560px;height:506px;background:linear-gradient(90deg,#b9b9b9 0%,#d8d8d8 55%,rgba(216,232,238,0) 100%)}
.hero-copy{position:absolute;left:500px;top:165px;width:600px;text-align:center;font-size:34px;font-weight:700;line-height:42px;color:var(--ink)}
.hero-copy .name{color:var(--title);font-size:40px}
.hero-btn{position:absolute;left:700px;top:360px;width:195px;height:66px;background:var(--cyan);color:var(--white);font-size:30px;font-weight:700;display:flex;align-items:center;justify-content:center;border-radius:3px;box-shadow:0 4px 6px rgba(0,0,0,.25)}
.dots{position:absolute;left:957px;top:479px;display:flex;gap:14px}
.dots span{width:16px;height:16px;border-radius:50%;background:#3d8fb8}
.dots span.on{background:var(--title)}
.hero-rule{left:0;top:667px;width:1200px;height:5px;background:var(--navy);z-index:3}
.chevron{left:562px;top:669px;width:74px;height:37px;overflow:hidden;z-index:3}
.chevron div{width:74px;height:74px;border-radius:50%;background:var(--navy);margin-top:-37px;display:flex;align-items:flex-end;justify-content:center;padding-bottom:9px}

/* services */
.services{left:0;top:672px;width:1200px;height:643px;background:linear-gradient(180deg,#e2f1f7 0%,#ffffff 40%)}
.section-title{position:absolute;left:0;width:1200px;text-align:center;top:52px;font-size:40px;font-weight:700;color:var(--title)}
.section-intro{position:absolute;left:112px;top:112px;width:976px;text-align:center;font-size:16px;line-height:20px;color:var(--muted)}
.grid-line-v{position:absolute;width:2px;background:linear-gradient(180deg,rgba(200,220,230,0),#dbe8ee 50%,rgba(200,220,230,0))}
.grid-line-h{position:absolute;height:2px;left:100px;width:995px;background:linear-gradient(90deg,rgba(200,220,230,0),#dbe8ee 50%,rgba(200,220,230,0))}
.service{position:absolute;width:320px;height:120px}
.service .icon{position:absolute;left:30px;top:0;width:98px;height:98px;border-radius:50%;background:radial-gradient(circle at 50% 40%,#ffffff 55%,#e2e8ec 100%);box-shadow:0 2px 4px rgba(0,0,0,.12);display:flex;align-items:center;justify-content:center}
.service .icon.filled{background:var(--navy)}
.service h3{position:absolute;left:146px;top:8px;font-size:20px;font-weight:400;color:var(--cyan-nav)}
.service h3.dark{color:var(--ink)}
.service p{position:absolute;left:148px;top:36px;width:165px;font-size:15px;line-height:20px;color:var(--muted)}

/* welcome band */
.welcome{left:0;top:1315px;width:1200px;height:299px;background:linear-gradient(180deg,#124f7c,#0e4470);color:var(--white)}
.welcome-photo{position:absolute;left:110px;top:57px;width:201px;height:199px;background:linear-gradient(135deg,#7b9bbd,#cfd7df 60%,#5c7d9e)}
.welcome h2{position:absolute;left:334px;top:54px;font-size:20px;font-weight:600}
.welcome h2 span{color:var(--cyan);font-weight:700}
.welcome .body{position:absolute;left:337px;top:94px;width:340px;font-size:16px;line-height:20px;font-weight:600}
.btn-small{position:absolute;left:562px;top:221px;width:109px;height:38px;background:var(--cyan);color:var(--white);font-size:16px;font-weight:700;display:flex;align-items:center;justify-content:center;border-radius:2px}
.welcome h3{position:absolute;left:766px;top:54px;font-size:20px;font-weight:400;color:var(--cyan)}
.quote{position:absolute;left:772px;top:103px;width:296px;height:84px;background:var(--cyan);font-size:16px;line-height:20px;padding:20px 18px}
.quote-tail{position:absolute;left:800px;top:187px;width:0;height:0;border-left:16px solid var(--cyan);border-bottom:16px solid transparent}
.client{position:absolute;left:774px;top:211px;font-size:16px}
.client span{color:var(--cyan)}

/* news */
.news{left:0;top:1614px;width:1200px;height:359px;background:linear-gradient(180deg,#ffffff 0%,#e4f1f6 100%)}
.news h2{position:absolute;left:110px;top:44px;font-size:38px;font-weight:700;color:var(--cyan)}
.news-item{position:absolute;top:144px;width:480px;height:140px}
.news-badge{position:absolute;left:0;top:0;width:126px;height:126px;border-radius:50%;background:var(--navy);display:flex;align-items:center;justify-content:center;color:var(--white);font-size:24px;font-weight:700}
.news-item h3{position:absolute;left:148px;top:4px;font-size:20px;font-weight:400;color:var(--cyan-nav)}
.news-item .date{position:absolute;left:148px;top:34px;font-size:16px}
.news-item p{position:absolute;left:148px;top:62px;width:300px;font-size:15px;line-height:20px;color:var(--muted)}

/* footer */
.footer{left:0;top:1973px;width:1200px;height:275px;background:linear-gradient(180deg,#0f3e66,#0b355a);color:var(--white)}
.footer h4{position:absolute;font-size:20px;font-weight:600}
.social{position:absolute;left:118px;top:64px;display:flex;gap:30px}
.social span{width:36px;height:36px;border-radius:50%;border:2px solid var(--white)}
.links{position:absolute;left:123px;top:152px;font-size:16px;line-height:34px;color:var(--cyan)}
.contact-row{position:absolute;left:454px;display:flex;align-items:flex-start;gap:14px;font-size:16px;letter-spacing:1px;line-height:29px;color:var(--cyan)}
.map{position:absolute;left:705px;top:64px;width:386px;height:120px;background:linear-gradient(135deg,#e8ecde,#d6dfe6 60%,#c3d3df);border:2px solid #4fb8de}
.bottombar{left:0;top:2248px;width:1200px;height:51px;background:var(--navy-deep);color:#cfd9e2;font-size:20px;display:flex;align-items:center;justify-content:center}
</style>
</head>
<body>

<div class="abs topbar">
  <div class="item" style="left:110px">
    <svg width="22" height="16" viewBox="0 0 22 16"><rect x="1" y="1" width="20" height="14" fill="none" stroke="#fff" stroke-width="2"/><path d="M1 1l10 8 10-8" fill="none" stroke="#fff" stroke-width="2"/></svg>
    halvernkeyworks.example
  </div>
  <div class="item" style="left:331px">
    <svg width="24" height="16" viewBox="0 0 24 16"><path d="M2 5c0-3 20-3 20 0v2h-5V5H7v2H2z" fill="#fff"/><rect x="5" y="8" width="14" height="7" rx="1" fill="#fff"/></svg>
    +123-555-0190
  </div>
  <div class="search">
    <div class="field">search</div>
    <div class="btn"><svg width="16" height="16" viewBox="0 0 16 16"><circle cx="6.5" cy="6.5" r="4.8" fill="none" stroke="#fff" stroke-width="2"/><path d="M10 10l5 5" stroke="#fff" stroke-width="2.4"/></svg></div>
  </div>
</div>

<header class="abs header">
  <div class="brand"><span class="mark"></span>Halvern Keyworks</div>
  <nav class="nav">
    <a class="active">Home</a>
    <a>About Us</a>
    <a>Services</a>
    <a>Locksmith services</a>
    <a>Price list</a>
    <a>Contact</a>
  </nav>
</header>

<section class="abs hero">
  <div class="hero-photo" role="img" aria-label="Hand holding a car key with remote head"></div>
  <h1 class="hero-copy"><span class="name">HALVERN KEYWORKS</span> provide recovery services and automotive lock-smith services to the Dallas Ft-Worth Area.</h1>
  <div class="hero-btn">Read more</div>
  <div class="dots"><span class="on"></span><span></span><span></span><span></span><span></span></div>
</section>
<div class="abs hero-rule"></div>
<div class="abs chevron"><div><svg width="26" height="16" viewBox="0 0 26 16"><path d="M3 3l10 10 10-10" fill="none" stroke="#fff" stroke-width="3.5"/></svg></div></div>

<section class="abs services">
  <h2 class="section-title">Our Services</h2>
  <p class="section-intro">Lorem Ipsum is simply dummy text of the printing and typesetting industry. Lorem Ipsum has been the industry's standard dummy text ever since the 1500s, when an unknown printer took a galley of type and scrambled it to make a type specimen book. It has survived not only five centuries</p>

  <div class="grid-line-v" style="left:430px;top:200px;height:420px"></div>
  <div class="grid-line-v" style="left:758px;top:200px;height:420px"></div>
  <div class="grid-line-h" style="top:414px"></div>

  <div class="service" style="left:100px;top:242px">
    <div class="icon filled"><svg width="64" height="40" viewBox="0 0 64 40"><path d="M4 26h34V14h10l8 8v4h4v6H4z" fill="#fff"/><path d="M30 14L12 4l-2 3 16 9" fill="#fff"/><circle cx="16" cy="32" r="5" fill="#fff" stroke="#0f4c78" stroke-width="2"/><circle cx="48" cy="32" r="5" fill="#fff" stroke="#0f4c78" stroke-width="2"/></svg></div>
    <h3 class="dark">Towing Services</h3>
    <p>Lorem Ipsum is simply dummy text of the printing and typeset-</p>
  </div>
  <div class="service" style="left:420px;top:242px">
    <div class="icon"><svg width="44" height="50" viewBox="0 0 44 50"><rect x="6" y="4" width="32" height="36" rx="4" fill="#111"/><rect x="11" y="9" width="22" height="13" fill="#fff"/><rect x="2" y="14" width="4" height="8" fill="#111"/><rect x="38" y="14" width="4" height="8" fill="#111"/><rect x="9" y="40" width="7" height="7" fill="#111"/><rect x="28" y="40" width="7" height="7" fill="#111"/><circle cx="13" cy="31" r="3" fill="#fff"/><circle cx="31" cy="31" r="3" fill="#fff"/></svg></div>
    <h3>Vehicle Transport</h3>
    <p>Lorem Ipsum is simply dummy text of the printing and typeset-</p>
  </div>
  <div class="service" style="left:754px;top:242px">
    <div class="icon"><svg width="50" height="50" viewBox="0 0 50 50"><circle cx="15" cy="10" r="6" fill="none" stroke="#111" stroke-width="3"/><path d="M21 10h18M33 10v5M38 10v4" stroke="#111" stroke-width="3"/><path d="M10 30l4-9h22l4 9v12h-5v-4H15v4h-5z" fill="#111"/><circle cx="16" cy="33" r="2.5" fill="#fff"/><circle cx="34" cy="33" r="2.5" fill="#fff"/></svg></div>
    <h3>Locksmith Service</h3>
    <p>Lorem Ipsum is simply dummy text of the printing and typeset-</p>
  </div>

  <div class="service" style="left:100px;top:456px">
    <div class="icon"><svg width="60" height="44" viewBox="0 0 60 44"><path d="M2 16h26v20H2zM28 22h10l6 7v7H28z" fill="#111"/><circle cx="11" cy="38" r="5" fill="#111" stroke="#fff" stroke-width="2"/><circle cx="36" cy="38" r="5" fill="#111" stroke="#fff" stroke-width="2"/><circle cx="46" cy="14" r="11" fill="#fff" stroke="#111" stroke-width="3"/><path d="M46 8v6l4 3" fill="none" stroke="#111" stroke-width="2.5"/></svg></div>
    <h3>Product Delivery</h3>
    <p>Lorem Ipsum is simply dummy text of the printing and typeset-</p>
  </div>
  <div class="service" style="left:420px;top:456px">
    <div class="icon"><svg width="50" height="50" viewBox="0 0 50 50"><path d="M25 4L4 18v28h42V18z" fill="#111"/><path d="M13 26h24v16H13z" fill="#fff"/><path d="M16 29h18v10H16z" fill="#111"/><path d="M16 34h18" stroke="#fff" stroke-width="2"/></svg></div>
    <h3>Free Storage</h3>
    <p>Lorem Ipsum is simply dummy text of the printing and typeset-</p>
  </div>
  <div class="service" style="left:754px;top:456px">
    <div class="icon"><svg width="50" height="50" viewBox="0 0 50 50"><path d="M8 12c2-3 6-4 8-2l4 6c1 2 0 4-2 5l-2 1c2 5 6 9 11 11l1-2c1-2 3-3 5-2l6 4c2 2 1 6-2 8-6 4-16 0-23-7S4 18 8 12z" fill="#111"/><path d="M28 4h16a4 4 0 014 4v10a4 4 0 01-4 4h-8l-5 4v-4h-3a4 4 0 01-4-4V8a4 4 0 014-4z" fill="#111"/><circle cx="31" cy="13" r="1.8" fill="#fff"/><circle cx="36" cy="13" r="1.8" fill="#fff"/><circle cx="41" cy="13" r="1.8" fill="#fff"/></svg></div>
    <h3>Customer Care</h3>
    <p>Lorem Ipsum is simply dummy text of the printing and typeset-</p>
  </div>
</section>

<section class="abs welcome">
  <div class="welcome-photo" role="img" aria-label="Hand holding a car key fob"></div>
  <h2>Welcome to <span>HALVERN KEYWORKS</span></h2>
  <p class="body">Lorem Ipsum is simply dummy text of the printing and typesetting industry. Lorem Ipsum has been the industry's standard dummy text ever since the 1500s, when an unknown printer took a .......</p>
  <div class="btn-small">Read more</div>
  <h3>What client's says</h3>
  <div class="quote">Lorem Ipsum is simply dummy text of the printing and typesetting industry.</div>
  <div class="quote-tail"></div>
  <div class="client"><span>Neque</span> porro quisquam</div>
</section>

<section class="abs news">
  <h2>Latest News</h2>
  <article class="news-item" style="left:126px">
    <div class="news-badge">QRT</div>
    <h3>Neque porro quisquam est</h3>
    <div class="date">12 october,2014</div>
    <p>Lorem Ipsum is simply dummy text of the printing and typesetting industry. Lorem Ipsum has been the industry's standard</p>
  </article>
  <article class="news-item" style="left:630px">
    <div class="news-badge">QRT</div>
    <h3>Neque porro quisquam est</h3>
    <div class="date">12 october,2014</div>
    <p>Lorem Ipsum is simply dummy text of the printing and typesetting industry. Lorem Ipsum has been the industry's standard</p>
  </article>
</section>

<footer class="abs footer">
  <h4 style="left:123px;top:22px">Follow Us</h4>
  <div class="social" aria-label="Social media links"><span></span><span></span><span></span><span></span></div>
  <h4 style="left:123px;top:116px">Important Links</h4>
  <div class="links">Our Services<br>Locksmith services<br>Price list</div>

  <h4 style="left:454px;top:22px">Contact Us</h4>
  <div class="contact-row" style="top:76px">
    <svg width="12" height="18" viewBox="0 0 12 18" style="margin-top:6px"><path d="M6 0a6 6 0 016 6c0 4-6 12-6 12S0 10 0 6a6 6 0 016-6z" fill="#1ab3e6"/><circle cx="6" cy="6" r="2.2" fill="#0f3e66"/></svg>
    <span>4120 CARROW BLVD<br>DALLAS, TX 75211</span>
  </div>
  <div class="contact-row" style="top:160px">
    <svg width="14" height="14" viewBox="0 0 14 14" style="margin-top:9px"><path d="M2 1c1-1 3 0 3 1l1 3-2 1c1 2 2 3 4 4l1-2 3 1c1 0 2 2 1 3-3 3-12-6-11-11z" fill="#1ab3e6"/></svg>
    <span>+888-555-0147</span>
  </div>
  <div class="contact-row" style="top:212px">
    <svg width="18" height="14" viewBox="0 0 18 14" style="margin-top:9px"><path d="M1 5l8-4 8 4v8H1z" fill="none" stroke="#1ab3e6" stroke-width="2"/><path d="M1 5l8 5 8-5" fill="none" stroke="#1ab3e6" stroke-width="2"/></svg>
    <span>contact@halvernkeyworks.example</span>
  </div>
  <div class="map" role="img" aria-label="Location map"></div>
</footer>

<div class="abs bottombar">All Rights Reserved@ 2014 contact@halvernkeyworks.example</div>

</body>
</html>
```